Brackenfold Health Web Page

We need a visually exciting webpage that introduces people to our practice. We are a practice that has both physiotherapy and psychology and we need the page to reflect this. We are also split across two practice locations. We need the page to be able to be updated regularly to include a blog spot and the linking in of our facebook page. There should be tabs to introduce our practitioners with some blurbs about them, a tab for people to be able to contact us, a tab to read about physiotherapy services and a tab to talk about psychology services. If there are other tabs than please include these. We are a practice that has treated world class athlete on a regular basis and see our selves as leaders in the field and the website must reflect this. I do not want basic clip-arty type things that anyone could have, we have to have something that draws people in.
Firstly, thanks everyone for their designs. I have attached some links to some physiotherapy websites that I think contain some interesting information and/or layout, as well as some comments,
Hi all,
Reason: Hi Guys,
We are so very close to finding a great design. I feel that we just need a bit of extra time to be able to clinch where we want to be. Thanks for your fantastic designs :)
Regards,
Oliver and Ruth
- 2 Practice Addresses (details to follow for right applications)
Psychology aspect
Physiotherapy aspect
Ability to update blog

```html
<!DOCTYPE html>
<html lang="en">
<head>
<meta charset="utf-8">
<title>Psychology – Brackenfold Health</title>
<link href="https://fonts.googleapis.com/css2?family=Mako&family=Arimo:wght@400;700&display=swap" rel="stylesheet">
<style>
:root{
  --white:#ffffff;
  --page:#f3f3f3;
  --nav:#e3e3e3;
  --nav-active:#d4d4d4;
  --teal:#2f9a98;
  --ink:#222222;
  --physio-blue:#2e5a8c;
  --psych-blue:#2a2aa0;
  --banner:#9b9bff;
  --panel:#f1f1f1;
  --strip:#e9e9e9;
  --avatar:#d9d9f5;
  --link:#8ab4e8;
  --booking:#a7d1fb;
  --field:#e3e3e3;
  --field-line:#9a9a9a;
  --footer:#c9c9c9;
  --leaf:#4aa84a;
  --illus:#8e8e8e;
  --social:#3b5b98;
}
*{box-sizing:border-box;margin:0;padding:0}
html,body{width:1200px;height:1186px;overflow:hidden}
body{position:relative;background:var(--page);font-family:"Mako",sans-serif;color:var(--ink)}
.abs{position:absolute}

.topbar{left:0;top:0;width:1200px;height:90px;background:var(--white)}
.contact-item{display:flex;align-items:center;gap:10px;font-size:16px;color:#333;top:26px;white-space:nowrap}
.social-square{left:1128px;top:27px;width:24px;height:24px;background:var(--social);border-radius:3px}

.nav{left:0;top:90px;width:1200px;height:68px;background:var(--nav);border-top:1px solid #d0d0d0;border-bottom:1px solid #d6d6d6}
.nav-link{font-family:"Arimo",sans-serif;font-size:17px;color:#111;top:34px;white-space:nowrap}
.nav-link.physio{color:var(--physio-blue)}
.nav-tab{left:602px;top:0;width:153px;height:68px;background:var(--nav-active);border-left:1px solid #bbb;border-right:1px solid #bbb;border-bottom:3px solid var(--teal)}
.nav-tab span{position:absolute;left:0;right:0;top:34px;text-align:center;font-family:"Arimo",sans-serif;font-size:17px;color:var(--psych-blue)}
.leaf{left:579px;top:48px;width:27px;height:20px;background:var(--leaf);border-radius:0 100% 0 100%}

.banner{left:0;top:215px;width:661px;height:44px}
.banner-title{left:148px;top:227px;font-size:17px;font-style:italic;font-weight:normal;color:var(--white);letter-spacing:.3px;white-space:nowrap}

.content-card{left:24px;top:306px;width:638px;height:579px;background:var(--white);border:2px solid #dedede;box-shadow:0 2px 2px rgba(0,0,0,.08)}
.content-panel{left:37px;top:316px;width:612px;height:549px;background:var(--panel)}
.section-header{left:67px;top:341px;font-size:15px;font-weight:normal;color:#222}
.paragraphs{left:65px;top:389px;width:540px;font-size:12.3px;line-height:14.7px;font-style:italic;color:#222}
.paragraphs p{margin-bottom:14.7px}
.paragraphs .gap{margin-bottom:29px}
.head-illustration{left:500px;top:711px;width:148px;height:153px;background:linear-gradient(135deg,#b9b9b9,var(--illus));border-radius:60% 50% 10% 20%}

.practitioners-title{left:757px;top:254px;font-size:17px;font-style:italic;font-weight:bold;letter-spacing:.5px;color:#222;white-space:nowrap}
.practitioner-strip{left:718px;top:287px;width:482px;height:161px;background:var(--strip);box-shadow:0 6px 8px -4px rgba(0,0,0,.25)}
.avatar{width:81px;height:79px;background:var(--avatar)}
.practitioner-name{font-size:15px;color:#222;text-align:center;width:140px}
.practitioner-role{font-size:13px;font-style:italic;color:#222;text-align:center;width:140px}
.more-link{font-size:12px;font-style:italic;color:var(--link)}

.booking-frame{left:715px;top:471px;width:461px;height:236px;background:var(--white);box-shadow:0 0 4px rgba(0,0,0,.08)}
.booking{left:726px;top:481px;width:440px;height:214px;background:var(--booking)}
.booking-title{right:54px;top:489px;font-size:14px;font-style:italic;color:#111}
.field{background:var(--field);border:1px solid var(--field-line);border-top-width:2px;font-size:14px;font-style:italic;color:#666;padding:3px 5px}
.submit{left:951px;top:647px;width:199px;height:38px;background:var(--teal);color:var(--white);font-family:"Arimo",sans-serif;font-weight:bold;font-size:16px;display:flex;align-items:center;justify-content:center;border-radius:2px}

.footer{left:0;top:1018px;width:1200px;height:168px;background:var(--footer);border-top:1px solid #b5b5b5}
.footer-links{left:0;width:1200px;top:1078px;text-align:center;font-size:16px;color:#444}
.footer-address{left:0;width:1200px;top:1114px;text-align:center;font-family:"Arimo",sans-serif;font-size:16px;color:#000}
</style>
</head>
<body>

<header class="abs topbar">
  <div class="abs contact-item" style="left:794px">
    <svg width="26" height="26" viewBox="0 0 26 26" aria-hidden="true"><rect x="1" y="1" width="24" height="24" rx="4" fill="#bdbdbd" stroke="#777"/><path d="M9 6c-2 1-2 4 0 8s5 6 7 6l2-2-3-3-2 1c-1-1-2-3-2-4l1-2-3-4z" fill="#333"/></svg>
    <span>1234567890</span>
  </div>
  <div class="abs contact-item" style="left:940px">
    <svg width="26" height="26" viewBox="0 0 26 26" aria-hidden="true"><rect x="1" y="1" width="24" height="24" rx="4" fill="#bdbdbd" stroke="#777"/><rect x="5" y="8" width="16" height="11" fill="#eee" stroke="#444"/><path d="M5 8l8 6 8-6" fill="none" stroke="#444"/></svg>
    <span>mail@bfhealth.com</span>
  </div>
  <div class="abs social-square" role="img" aria-label="Social page link"></div>
</header>

<nav class="abs nav">
  <span class="abs nav-link" style="left:221px">HOME</span>
  <span class="abs nav-link" style="left:330px">ABOUT</span>
  <span class="abs nav-link physio" style="left:428px">PHYSIOTHERAPY</span>
  <div class="abs leaf" role="img" aria-label="Small leaf accent"></div>
  <div class="abs nav-tab"><span>PSYCHOLOGY</span></div>
  <span class="abs nav-link" style="left:805px;top:30px">PRACTITIONERS</span>
  <span class="abs nav-link" style="left:990px">BLOG</span>
  <span class="abs nav-link" style="left:1092px">CONTACT</span>
</nav>

<svg class="abs banner" viewBox="0 0 661 44" aria-hidden="true"><polygon points="0,0 616,0 661,44 0,44" fill="var(--banner)"/></svg>
<h1 class="abs banner-title">PSYCHOLOGY AT BRACKENFOLD HEALTH</h1>

<section>
  <div class="abs content-card"></div>
  <div class="abs content-panel"></div>
  <h2 class="abs section-header">SECTION HEADER</h2>
  <div class="abs paragraphs">
    <p>PARAGRAPH 1<br>Lorem ipsum dolor sit amet, ac purus, tellus wisi vitae alias duis class, semper nascetur, aenean condimentum ipsa mattis mollis nisl lacus, libero leo interdum metus aliquam. Congue iaculis a lob-ortis eleifend, id fermentum proin ac tincidunt, vehicula mi urna. Mattis id arcu. Eu vestibulum, metus erat integer commodo augue porttitor, amet fusce mauris maecenas tortor libero, augue diam sollicitudin aliquam magna tellus, et in et wisi.<br>PARAGRAPH 2<br>Eros sociosqu aenean suspendisse duis, et sapien egestas non, ullam ante netus arcu elit leo suscip-it. Varius faucibus, fermentum vehicula dolor auctor. Massa eu ut semper et elementum, neque ipsum, orci consectetuer diam maecenas, vehicula eros enim. Libero aliquam aenean sodales nullam, massa egestas posuere massa sollicitudin, habitant at eleifend pellentesque.</p>
    <p class="gap">PARAGRAPH 3<br>Lacus justo accumsan libero, tincidunt laoreet pellentesque aliquam, metus velit nibh nec dolor felis nulla, nulla enim. Imperdiet in cras sapien imperdiet. Faucibus tempor semper accumsan sapien fringilla, dolor non posuere donec et integer turpis, enim proin nunc.</p>
    <p>PARAGRAPH 4<br>Senectus velit, nibh ad donec sem pretium, velit porta fusce, ultrices turpis sed elementum nam, lacus lobortis massa vestibulum. Orci dolor potenti malesuada vitae luctus integer, donec enim ante, enim dolor eu, enim sapien vestibulum enim urna.</p>
  </div>
  <div class="abs head-illustration" role="img" aria-label="Illustration of a head in profile made of puzzle pieces"></div>
</section>

<aside>
  <h2 class="abs practitioners-title">Our Psychology Practitioners</h2>
  <div class="abs practitioner-strip"></div>
  <div class="abs avatar" style="left:755px;top:290px" role="img" aria-label="Practitioner photo placeholder"></div>
  <div class="abs practitioner-name" style="left:721px;top:373px">Ruth Hallam</div>
  <div class="abs practitioner-role" style="left:721px;top:393px">Psychologist</div>
  <span class="abs more-link" style="left:823px;top:418px">more &gt;</span>
  <div class="abs avatar" style="left:919px;top:290px" role="img" aria-label="Practitioner photo placeholder"></div>
  <div class="abs practitioner-name" style="left:896px;top:380px">Name Surname</div>
  <div class="abs practitioner-role" style="left:893px;top:398px">Psychologist</div>
  <span class="abs more-link" style="left:973px;top:420px">more &gt;</span>

  <div class="abs booking-frame"></div>
  <form class="abs booking"></form>
  <div class="abs booking-title">BOOK A MEETING</div>
  <div class="abs field" style="left:736px;top:519px;width:200px;height:25px">Name</div>
  <div class="abs field" style="left:736px;top:570px;width:200px;height:25px">E-mail</div>
  <div class="abs field" style="left:736px;top:616px;width:200px;height:25px">Phone number</div>
  <div class="abs field" style="left:950px;top:518px;width:200px;height:123px;line-height:17px">Short description of your health issue</div>
  <div class="abs submit">SUBMIT</div>
</aside>

<footer class="abs footer"></footer>
<div class="abs footer-links">Home - About -Physiotherapy - Psychology - Practitioners - Blog - Contact</div>
<div class="abs footer-address">24 Linden Rd, Ashvale QLD 4361 Australia</div>

</body>
</html>
```